Business Card Design

Our Motto is "Protecting Australia's Underground Utilities"

We want the Southern Cross inside a shield I have attached the southern cross and our old shield design

Product description is: Vacuum Excavation & Utility Location
Wet & Dry Vacuum Loading
Confined Space Entry Specialists
High Pressure Cleaning

The Southern Cross in the shield must be blue and white. The Company name must be Coastal Pipeguard Services. The Green & Gold Shield logo I uploaded is my OLD logo design. Thank you

Target Market(s)

Civil Construction

Industry/Entity Type

Business

Contact Information for Business Card

Coastal Pipeguard Services Pty Ltd
Corey Halbrook(Director)
0413862975
coreyh@pipeguardco.com.au
A.B.N.52938470116

Colors
0456a3

Requirements
Must have
• Southern Cross inside a shield, Blue and white design on the Southern Cross shield.
Must say Coastal Pipeguard Services P/L

```html
<!DOCTYPE html>
<html lang="en">
<head>
<meta charset="utf-8">
<title>Coastal Pipeguard Services – Business Card</title>
<link rel="stylesheet" href="https://fonts.googleapis.com/css2?family=Audiowide&family=Open+Sans:wght@400;700&display=swap">
<style>
  :root {
    --stage: #3b2517;
    --paper: #ffffff;
    --brand-green: #33dd00;
    --brand-blue: #3a55e6;
    --ink: #1a1a1a;
    --rule: #333333;
  }
  * { box-sizing: border-box; margin: 0; padding: 0; }
  html, body {
    width: 1200px; height: 490px; overflow: hidden;
    background: var(--stage);
  }
  .canvas {
    position: relative; width: 1200px; height: 490px;
  }
  .card {
    position: absolute; top: 80px;
    width: 540px; height: 330px;
    background: var(--paper);
    overflow: hidden;
  }
  .card--front { left: 40px; }
  .card--back { left: 620px; }

  .front-sweep { position: absolute; inset: 0; }

  .holder {
    position: absolute; top: 22px; right: 34px;
    text-align: right; color: var(--paper);
    font-family: "Open Sans", sans-serif;
  }
  .holder__name { font-weight: 700; font-size: 20px; line-height: 1.1; }
  .holder__role { font-size: 14px; margin-top: 2px; }

  .wordmark {
    position: absolute; left: 38px; bottom: 40px;
    font-family: "Audiowide", sans-serif;
    color: var(--brand-green);
    font-size: 19px; line-height: 1.1;
  }
  .wordmark__mark {
    width: 70px; height: 70px;
    background: var(--brand-green);
    margin: 0 0 16px 40px;
  }
  .divider {
    position: absolute; left: 236px; bottom: 46px;
    width: 1px; height: 48px; background: var(--rule);
  }
  .contact {
    position: absolute; left: 250px; bottom: 48px;
    font-family: "Open Sans", sans-serif;
    font-size: 14px; color: var(--ink);
    list-style: none;
  }
  .contact li { display: flex; align-items: center; gap: 6px; line-height: 24px; }
  .contact svg { width: 13px; height: 13px; }

  .back-mark {
    position: absolute; left: 58px; top: 92px;
    width: 140px; height: 150px;
    background: var(--brand-blue);
  }
  .company {
    position: absolute; left: 230px; top: 128px;
    font-family: "Audiowide", sans-serif;
    color: var(--ink); font-size: 19px; line-height: 1.1;
  }
  .company__abn {
    color: var(--brand-green); font-size: 15px; margin-top: 12px;
  }
</style>
</head>
<body>
<main class="canvas">
  <section class="card card--front">
    <svg class="front-sweep" viewBox="0 0 540 330" preserveAspectRatio="none" aria-hidden="true">
      <path d="M0,0 H540 V240 C480,80 260,18 0,22 Z" fill="var(--brand-green)"/>
      <path d="M0,36 C260,32 480,96 540,262" fill="none" stroke="var(--brand-blue)" stroke-width="6"/>
    </svg>
    <div class="holder">
      <p class="holder__name">Corey Halbrook</p>
      <p class="holder__role">Director</p>
    </div>
    <div class="wordmark">
      <div class="wordmark__mark"></div>
      <p>Coastal Pipeguard<br>Services</p>
    </div>
    <div class="divider"></div>
    <ul class="contact">
      <li>
        <svg viewBox="0 0 16 16" aria-hidden="true"><circle cx="8" cy="8" r="7" fill="none" stroke="currentColor" stroke-width="1.5"/><path d="M5 4.5l2 2-1 1c.6 1.2 1.3 1.9 2.5 2.5l1-1 2 2-1.2 1.2C7 12 4 9 3.8 5.7Z" fill="currentColor"/></svg>
        0413862975
      </li>
      <li>
        <svg viewBox="0 0 16 16" aria-hidden="true"><rect x="1.5" y="4" width="13" height="9" rx="1" fill="currentColor"/><path d="M2 5l6 4 6-4" fill="none" stroke="#fff" stroke-width="1.2"/></svg>
        coreyh@pipeguardco.com.au
      </li>
    </ul>
  </section>

  <section class="card card--back">
    <div class="back-mark"></div>
    <div class="company">
      <p>Coastal Pipeguard<br>Services Pty Ltd</p>
      <p class="company__abn">A.B.N.52938470116</p>
    </div>
  </section>
</main>
</body>
</html>
```